Hi,

I would like to have a invitation made for a party. exactly like the picture in the link below.

http://pinboardia.example/pin/730215948361027459/

However, Please change the colors into fun/ girly feeling. font can be different and size of the card should be the same

Name of the girl: RINA
What: Bachelorette Party
Where:TOLO Boat
Dubai Coral Quay Sailing Club
When:7th of February 2013

No RSVP required. (so no need to put it)

```html
<!DOCTYPE html>
<html lang="en">
<head>
<meta charset="utf-8">
<title>Rina's Bachelorette Invitation</title>
<link rel="stylesheet" href="https://fonts.googleapis.com/css2?family=Pinyon+Script&family=Sancreek&family=Lato:wght@300;400&display=swap">
<style>
  :root {
    --page: #ffffff;
    --card: #fff5f9;
    --hot-pink: #ff3d94;
    --raspberry: #d81b6a;
    --plum: #7b2760;
    --bubblegum: #ffb6d5;
    --peach-pink: #ff8fba;
    --blush: #ffd9e8;
    --fold-line: #ff9cc6;
    --frame: #e0488c;
  }
  html, body {
    margin: 0;
    padding: 0;
    width: 1200px;
    height: 766px;
    overflow: hidden;
    background: var(--page);
  }
  .canvas {
    position: relative;
    width: 1200px;
    height: 766px;
    background: var(--page);
    font-family: "Lato", sans-serif;
    color: var(--plum);
  }
  .card {
    position: absolute;
    left: 45px;
    top: 50px;
    width: 1099px;
    height: 654px;
    border: 1.5px solid var(--frame);
    box-sizing: border-box;
    background: var(--card);
  }
  .fold {
    position: absolute;
    top: 0;
    bottom: 0;
    width: 0;
    border-left: 1.5px solid var(--fold-line);
  }
  .fold--first { left: 366px; }
  .fold--second { left: 732px; }

  .guest-name {
    position: absolute;
    left: 14px;
    top: 22px;
    margin: 0;
    font-family: "Pinyon Script", cursive;
    font-weight: 400;
    font-size: 132px;
    line-height: 1;
    white-space: nowrap;
    color: var(--raspberry);
  }
  .tagline {
    position: absolute;
    top: 207px;
    margin: 0;
    font-family: "Lato", sans-serif;
    font-weight: 300;
    font-size: 35px;
    letter-spacing: 0.5px;
    line-height: 1;
    white-space: nowrap;
    color: var(--plum);
  }
  .tagline--left { left: 34px; }
  .tagline--middle { left: 384px; }

  .headline-letter {
    position: absolute;
    top: 361px;
    font-family: "Sancreek", serif;
    font-size: 215px;
    line-height: 1;
    color: var(--hot-pink);
    transform: translateX(-50%) scaleX(0.82);
    transform-origin: center;
  }

  .ornament {
    position: absolute;
    background: var(--blush);
    border-radius: 40px;
  }
  .ornament--crest { left: 431px; top: 87px; width: 246px; height: 104px; background: var(--bubblegum); }
  .ornament--fleuron { left: 134px; top: 292px; width: 84px; height: 58px; background: var(--peach-pink); border-radius: 28px; }
  .ornament--border { left: 0; top: 566px; width: 1096px; height: 67px; border-radius: 30px; background: var(--bubblegum); }

  .details {
    position: absolute;
    left: 778px;
    top: 116px;
    width: 267px;
    height: 358px;
    border: 2px solid var(--peach-pink);
    border-radius: 12px;
    box-sizing: border-box;
    text-align: center;
    background: var(--page);
  }
  .details__heading {
    margin: 34px 0 0;
    font-family: "Sancreek", serif;
    font-weight: 400;
    font-size: 40px;
    line-height: 50px;
    color: var(--hot-pink);
  }
  .details__block {
    margin: 30px 0 0;
    font-size: 18px;
    line-height: 26px;
    color: var(--plum);
  }
  .details__block + .details__block { margin-top: 34px; }
</style>
</head>
<body>
<main class="canvas">
  <section class="card" aria-label="Bachelorette party invitation">
    <div class="fold fold--first"></div>
    <div class="fold fold--second"></div>

    <div class="ornament ornament--crest" role="img" aria-label="Pink floral crest ornament"></div>
    <div class="ornament ornament--border" role="img" aria-label="Pink scrollwork border running along the bottom"></div>

    <h1 class="guest-name">Rina's</h1>
    <p class="tagline tagline--left">LAST CHANCE TO</p>
    <p class="tagline tagline--middle">CELEBRATE BEING</p>

    <div class="headline" aria-label="SINGLE">
      <span class="headline-letter" style="left:67px" aria-hidden="true">S</span>
      <span class="headline-letter" style="left:155px" aria-hidden="true">I</span>
      <span class="headline-letter" style="left:280px" aria-hidden="true">N</span>
      <span class="headline-letter" style="left:459px" aria-hidden="true">G</span>
      <span class="headline-letter" style="left:560px" aria-hidden="true">L</span>
      <span class="headline-letter" style="left:652px" aria-hidden="true">E</span>
    </div>

    <div class="ornament ornament--fleuron" role="img" aria-label="Small pink fleuron ornament"></div>

    <aside class="details">
      <h2 class="details__heading">YOUR<br>INVITED</h2>
      <p class="details__block">Where:<br>TOLO Boat<br>Dubai Coral Quay Sailing Club</p>
      <p class="details__block">When:<br>7th of February 2013</p>
    </aside>
  </section>
</main>
</body>
</html>
```